Conservative, Modern and Sharp Builder Business card

Hi there,
We would like to update our existing business card.
I have attached photos of existing business card, logo and van sign.

I would like the business card to also list what we do :
Renovation • New Build • Alteration
Extension • Bathroom • Maintenance.(Seperated by dots)

Contact number : 021 0483 0752
(With that exact spacing)

Ideally when people looking from about 2-3 metres, they know that it is a builder’s business card

Open to suggestions on fonts, layout, style of business card

PLEASE ONLY SUBMIT YOUR BEST OR MAX 3 DESIGNS FOR EACH DESIGNER

Thanks

Industry/Entity Type

Construction. Renovation

Contact Information for Business Card

Details should be the same as the existing card. And addition of what we do.

Requirements
Should not have
• The new business card must not have the same layout as our existing one. Thanks

```html
<!DOCTYPE html>
<html lang="en">
<head>
<meta charset="utf-8">
<title>KeelHouse Business Card</title>
<link href="https://fonts.googleapis.com/css2?family=Jost:wght@400;500;700&display=swap" rel="stylesheet">
<style>
  :root {
    --backdrop: #e4e4e6;
    --ink: #0d0d0d;
    --charcoal: #151515;
    --steel: #6b6b6b;
    --paper: #ffffff;
    --mist: #d8d8d8;
  }
  * { margin: 0; padding: 0; box-sizing: border-box; }
  html, body { width: 1200px; height: 800px; overflow: hidden; }
  body {
    background: var(--backdrop);
    font-family: "Jost", "Helvetica Neue", Arial, sans-serif;
    position: relative;
  }
  .card {
    position: absolute;
    width: 540px;
    height: 309px;
    overflow: hidden;
    box-shadow: 0 6px 18px rgba(0,0,0,0.18);
  }
  .card-back { left: 40px; top: 246px; background: var(--charcoal); }
  .card-front { left: 620px; top: 246px; background: var(--paper); }

  .back-pattern {
    position: absolute; inset: 0;
    background: linear-gradient(135deg, #1c1c1c 0%, #111 50%, #1c1c1c 100%);
  }
  .back-mark {
    position: absolute; right: 34px; bottom: 30px;
    display: flex; align-items: center; gap: 8px;
    color: var(--paper); font-weight: 700; font-size: 26px;
  }
  .mark-square { width: 12px; height: 12px; background: currentColor; }

  .front-shapes { position: absolute; inset: 0; }
  .holder {
    position: absolute; left: 26px; top: 22px; color: var(--paper);
  }
  .holder-name { font-weight: 500; font-size: 17px; letter-spacing: 1.5px; line-height: 1.15; }
  .holder-role { font-size: 12.5px; color: var(--mist); }
  .holder-phone {
    position: absolute; left: 26px; top: 74px;
    display: flex; align-items: center; gap: 8px;
    color: var(--paper); font-weight: 700; font-size: 19px; letter-spacing: 1.5px;
  }
  .contact-list {
    position: absolute; left: 26px; bottom: 26px;
    list-style: none; color: var(--paper); font-size: 13px;
  }
  .contact-list li { display: flex; align-items: center; gap: 8px; line-height: 21px; }
  .contact-list svg { width: 13px; height: 13px; }
  .social-dot { width: 12px; height: 12px; border: 1.5px solid var(--paper); border-radius: 50%; }

  .brand {
    position: absolute; right: 30px; top: 92px;
    display: flex; align-items: center; gap: 8px;
    color: var(--ink); font-weight: 700; font-size: 30px;
  }
  .services {
    position: absolute; right: 26px; top: 178px;
    text-align: right; color: var(--ink);
    font-weight: 700; font-size: 13.5px; line-height: 21px;
  }
</style>
</head>
<body>
  <section class="card card-back">
    <div class="back-pattern" role="img" aria-label="Tonal repeating pattern of the company monogram"></div>
    <div class="back-mark"><span class="mark-square"></span>KeelHouse</div>
  </section>

  <section class="card card-front">
    <svg class="front-shapes" viewBox="0 0 540 309" width="540" height="309" aria-hidden="true">
      <polygon points="0,0 380,0 370,40 300,309 0,309" fill="var(--charcoal)"/>
      <polygon points="0,18 318,18 342,42 318,66 0,66" fill="var(--steel)"/>
      <polygon points="318,18 380,0 380,40 342,42" fill="#3a3a3a"/>
    </svg>
    <div class="holder">
      <div class="holder-name">DARIO WHETU</div>
      <div class="holder-role">Residential Builder</div>
    </div>
    <div class="holder-phone">
      <svg width="14" height="16" viewBox="0 0 14 16" aria-hidden="true"><path d="M3 1 L6 4 L4.5 6 Q6 10 9 11.5 L11 10 L13.5 13 L11.5 15 Q4 14 1 3 Z" fill="none" stroke="var(--paper)" stroke-width="1.5"/></svg>
      021 0483 0752
    </div>
    <ul class="contact-list">
      <li><svg viewBox="0 0 13 13" aria-hidden="true"><rect x="1" y="3" width="11" height="8" fill="none" stroke="var(--paper)" stroke-width="1.4"/><path d="M1 3 L6.5 8 L12 3" fill="none" stroke="var(--paper)" stroke-width="1.4"/></svg>hello@keelhouse.nz</li>
      <li><svg viewBox="0 0 13 13" aria-hidden="true"><circle cx="6.5" cy="6.5" r="5.3" fill="none" stroke="var(--paper)" stroke-width="1.4"/><path d="M1.2 6.5 H11.8 M6.5 1.2 Q3.5 6.5 6.5 11.8 Q9.5 6.5 6.5 1.2" fill="none" stroke="var(--paper)" stroke-width="1.1"/></svg>www.KeelHouse.nz</li>
      <li><span class="social-dot"></span>KeelHouse.nz</li>
    </ul>
    <div class="brand"><span class="mark-square"></span>KeelHouse</div>
    <div class="services">
      <div>Renovation | New Build •</div>
      <div>Alteration | Extension •</div>
      <div>Bathroom | Maintenance •</div>
    </div>
  </section>
</body>
</html>
```